Company Proposal Powerpoint Template

We would like to update our overall proposal presentation with a fresh, new look that might appeal to the younger generation. We are a full-meeting management company that specializes in corporate events sales meetings, incentive trips, and tradeshows/conferences.
We have a core set of slides that we use for presentations, but will also need to customize based on the customers we service and what we are selling each potential client.
We have a company logo, but we are not tied into the colors schemes for the logo and are okay adding the logo in black or white versus in color.
I have included our current look and feel for this presentation. This will also give you content that we typically add to this presentation.
Reason: Traveling out of the office so limited access to review the art.
Industry/Entity Type
It Company
Look and feel
Each slider illustrates characteristics of the customer's brand and the style your logo design should communicate.

```html
<!DOCTYPE html>
<html lang="en">
<head>
<meta charset="utf-8">
<title>Meridian Events – Proposal Slides</title>
<link rel="stylesheet" href="https://fonts.googleapis.com/css2?family=Arimo:wght@400;700&family=Raleway:wght@300;400&display=swap">
<style>
  :root{
    --page:#ececec;
    --ink:#262626;
    --dark:#2a2a2a;
    --blue:#1e9be6;
    --blue-deep:#2a5d96;
    --ring:#b9c4d4;
    --band:#efefef;
    --white:#ffffff;
    --logo:#8c1d2c;
  }
  *{box-sizing:border-box;margin:0;padding:0}
  html,body{width:1200px;height:960px;overflow:hidden;background:var(--page)}
  body{position:relative;font-family:"Arimo",Arial,sans-serif;color:var(--ink)}

  .slide{position:absolute;width:553px;height:426px;transform:scale(.9375);transform-origin:0 0;background:var(--white);overflow:hidden}
  .slide--pricing{left:53px;top:74px}
  .slide--services{left:628px;top:74px}
  .slide--registration{left:353px;top:520px}

  .slide__header{position:absolute;left:0;top:0;width:553px;height:47px}
  .slide__header svg{position:absolute;inset:0}
  .slide__tag,.slide__title{position:absolute;top:9px;font-family:"Raleway",sans-serif;font-weight:300;font-size:26px;color:var(--white);letter-spacing:.5px;line-height:30px}
  .slide__title{right:22px}
  .slide__tag{left:105px}
  .slide__band-top{position:absolute;left:0;top:47px;width:100%;height:21px;background:var(--band)}
  .slide__band-bottom{position:absolute;left:0;top:383px;width:100%;height:35px;background:var(--band)}
  .slide__bar{position:absolute;left:0;top:418px;width:100%;height:8px;background:var(--blue)}

  .brand{position:absolute;display:flex;align-items:center;gap:5px;font-family:"Arimo",sans-serif;font-size:13px;color:var(--logo)}
  .brand__mark{width:11px;height:11px;background:var(--logo)}

  /* Pricing */
  .pillar{position:absolute;top:151px;width:110px;height:172px}
  .pillar svg{position:absolute;left:0;top:0;overflow:visible}
  .pillar__text{position:absolute;left:10px;top:37px;width:96px;font-size:8.6px;line-height:11px;color:var(--white)}
  .pillar__label{position:absolute;top:330px;width:110px;text-align:center;font-weight:700;font-size:10.5px;line-height:12.5px;color:var(--blue)}

  /* Services */
  .cycle{position:absolute;left:33px;top:128px}
  .cycle__label{font-family:"Arimo",sans-serif;font-weight:700;font-size:7.6px;fill:var(--white)}
  .solution{position:absolute;left:34px;top:349px;font-weight:700;font-size:10.5px;color:var(--blue)}
  .service-list{position:absolute;left:268px;top:98px;width:280px}
  .service{margin-bottom:22px}
  .service__head{font-weight:700;font-size:10px;color:var(--blue);line-height:12px}
  .service__body{font-size:8.6px;line-height:10.8px;color:var(--ink)}

  /* Registration */
  .turnkey{position:absolute;left:27px;top:123px;width:209px;height:235px;background:var(--dark)}
  .turnkey__head{height:34px;background:var(--blue);padding:6px 19px;font-weight:700;font-size:10.5px;line-height:12.5px;color:var(--white)}
  .turnkey__body{padding:20px 19px 0;font-size:8.4px;line-height:10.1px;color:#e6e6e6}
  .turnkey__body p{margin-bottom:10px}
  .sample{position:absolute;box-shadow:0 0 0 1px #d0d0d0}
  .sample--badge{left:287px;top:99px;width:78px;height:110px;background:linear-gradient(#6c5fb6,#8c7fc9)}
  .sample--site{left:409px;top:96px;width:80px;height:121px;background:linear-gradient(#e8e8e8,#fafafa 30%,#f2f2f2)}
  .sample--page{left:280px;top:235px;width:108px;height:120px;background:linear-gradient(#7a93b8,#d9e1ea 55%,#f4f4f4)}
  .sample--names{left:429px;top:238px;width:64px;height:110px;background:linear-gradient(#f6f6f6,#e9eef3)}
</style>
</head>
<body>

<section class="slide slide--pricing">
  <div class="slide__header">
    <svg width="553" height="47" viewBox="0 0 553 47" aria-hidden="true">
      <rect width="553" height="47" fill="#1e9be6"/>
      <polygon points="300,0 420,0 360,47" fill="#ffffff" opacity=".08"/>
      <polygon points="430,0 553,0 553,47 490,47" fill="#ffffff" opacity=".06"/>
      <path d="M0,47 Q10,10 45,0 L159,0 L159,47 Z" fill="#222"/>
      <polygon points="40,0 110,0 70,47 20,47" fill="#444" opacity=".6"/>
    </svg>
    <div class="slide__title">PRICING STRUCTURE</div>
  </div>
  <div class="slide__band-top"></div>
  <div class="brand" style="left:232px;top:102px"><span class="brand__mark"></span>Meridian Events</div>

  <div class="pillar" style="left:23px">
    <svg width="110" height="172" aria-hidden="true"><polygon points="0,25 110,25 160,0 50,0" fill="#111"/><polygon points="0,25 110,25 110,140 55,170 0,140" fill="#2b2b2b"/></svg>
    <div class="pillar__text">Dedicated Program Director<br>One Point of Delivering a Successful Program;<br>No matter what it takes<br>Fixed, Flat Fee;<br>No surprises on the final bill</div>
  </div>
  <div class="pillar" style="left:160px">
    <svg width="110" height="172" aria-hidden="true"><polygon points="0,25 110,25 117,0 50,0" fill="#111"/><polygon points="0,25 110,25 110,140 55,170 0,140" fill="#2b2b2b"/></svg>
    <div class="pillar__text">Custom Reporting/<br>Report Management<br>Call Center for email and phone inquiries<br>Billed on Actuals</div>
  </div>
  <div class="pillar" style="left:293px">
    <svg width="110" height="172" aria-hidden="true"><polygon points="0,25 110,25 110,0 -7,0" fill="#111"/><polygon points="0,25 110,25 110,140 55,170 0,140" fill="#2b2b2b"/></svg>
    <div class="pillar__text" style="left:14px;width:90px">Fully Trained,<br>Experienced Staff<br>on 24/7<br>Billed on Actuals</div>
  </div>
  <div class="pillar" style="left:430px">
    <svg width="110" height="172" aria-hidden="true"><polygon points="0,25 110,25 58,0 -52,0" fill="#111"/><polygon points="0,25 110,25 110,140 55,170 0,140" fill="#2b2b2b"/></svg>
    <div class="pillar__text" style="left:18px;width:88px">Worldwide Vendor Network<br>Pass-Through Costs; no mark up!</div>
  </div>

  <div class="pillar__label" style="left:23px">MEETING<br>MANAGEMENT</div>
  <div class="pillar__label" style="left:160px">ON-LINE<br>REGISTRATION<br>&amp; MOBILE APP</div>
  <div class="pillar__label" style="left:293px">ON-SITE<br>STAFFING</div>
  <div class="pillar__label" style="left:430px">THIRD<br>PARTY<br>SUPPLIERS</div>

  <div class="slide__band-bottom"></div>
  <div class="slide__bar"></div>
</section>

<section class="slide slide--services">
  <div class="slide__header">
    <svg width="553" height="47" viewBox="0 0 553 47" aria-hidden="true">
      <rect width="553" height="47" fill="#1e9be6"/>
      <polygon points="260,0 380,0 320,47" fill="#ffffff" opacity=".08"/>
      <polygon points="420,0 553,0 553,47 470,47" fill="#ffffff" opacity=".06"/>
      <path d="M0,47 Q10,10 45,0 L159,0 L159,47 Z" fill="#222"/>
      <polygon points="40,0 110,0 70,47 20,47" fill="#444" opacity=".6"/>
    </svg>
    <div class="slide__tag">ME</div>
    <div class="slide__title">WHAT WE DO</div>
  </div>
  <div class="slide__band-top"></div>
  <div class="brand" style="left:20px;top:96px"><span class="brand__mark"></span>Meridian Events</div>

  <svg class="cycle" width="200" height="200" viewBox="-100 -100 200 200" aria-hidden="true">
    <circle r="92" fill="none" stroke="#b9c4d4" stroke-width="10"/>
    <polygon points="2,-102 14,-92 2,-82" fill="#b9c4d4"/>
    <polygon points="88,53 82,68 72,50" fill="#b9c4d4"/>
    <polygon points="-90,53 -72,48 -80,66" fill="#b9c4d4"/>
    <g fill="#2a5d96" stroke="#fff" stroke-width="4">
      <path d="M0 0 L0 -84 A84 84 0 0 1 72.7 42 Z"/>
      <path d="M0 0 L72.7 42 A84 84 0 0 1 -72.7 42 Z"/>
      <path d="M0 0 L-72.7 42 A84 84 0 0 1 0 -84 Z"/>
    </g>
    <text class="cycle__label" x="-40" y="-22" text-anchor="middle">ONSITE EVENT</text>
    <text class="cycle__label" x="-40" y="-12" text-anchor="middle">MANAGEMENT</text>
    <text class="cycle__label" x="38" y="-27" text-anchor="middle">EVENT</text>
    <text class="cycle__label" x="38" y="-17" text-anchor="middle">MANAGEMENT</text>
    <text class="cycle__label" x="38" y="-7" text-anchor="middle">SERVICES</text>
    <text class="cycle__label" x="0" y="48" text-anchor="middle">REGISTRATION</text>
    <text class="cycle__label" x="0" y="58" text-anchor="middle">SERVICES</text>
  </svg>
  <div class="solution">FULL SERVICE MEETING SOLUTION</div>

  <div class="service-list">
    <div class="service">
      <div class="service__head">EVENT MANAGEMENT SERVICES</div>
      <div class="service__body">Overall Logistics &amp; Event Coordination, BEOs, Timelines<br>Supplier Management, Contracting, Payment Schedules<br>Conference/Program Promotion, Marketing Plans<br>Production, Entertainment, Speakers<br>Tradeshow Management, Sponsor &amp; Exhibit Sales<br>Air Ticketing &amp; Ground Transportation<br>Off-Site Events, including Tours &amp; Recreational Activities<br>Financial Management &amp; Post-Program Reconciliation<br>Gifts, Amenities, Awards, Hospitality Desks, Team Buildings, and more…</div>
    </div>
    <div class="service">
      <div class="service__head">REGISTRATION SERVICES</div>
      <div class="service__body">Website Design &amp; Development<br>Online Registration Turnkey Services: Licensed Platforms to select from include EventLoop, Regiflow, and SignPoint<br>Housing/Registration Management, including call centers</div>
    </div>
    <div class="service">
      <div class="service__head">ONSITE EVENT MANAGEMENT</div>
      <div class="service__body">Uniformed, Resourceful and Experienced On-Site Staff<br>Available 24/7 while on-site</div>
    </div>
  </div>

  <div class="slide__band-bottom"></div>
  <div class="slide__bar"></div>
</section>

<section class="slide slide--registration">
  <div class="slide__header">
    <svg width="553" height="47" viewBox="0 0 553 47" aria-hidden="true">
      <rect width="553" height="47" fill="#1e9be6"/>
      <polygon points="250,0 370,0 310,47" fill="#ffffff" opacity=".08"/>
      <polygon points="420,0 553,0 553,47 470,47" fill="#ffffff" opacity=".06"/>
      <path d="M0,47 Q10,10 45,0 L159,0 L159,47 Z" fill="#222"/>
      <polygon points="40,0 110,0 70,47 20,47" fill="#444" opacity=".6"/>
    </svg>
    <div class="slide__tag" style="left:27px">TURNKEY</div>
    <div class="slide__title">REGISTRATION SERVICES</div>
  </div>
  <div class="slide__band-top"></div>
  <div class="brand" style="left:33px;top:95px"><span class="brand__mark"></span>Meridian Events</div>

  <div class="turnkey">
    <div class="turnkey__head">TURNKEY REGISTRATION<br>SERVICES</div>
    <div class="turnkey__body">
      <p>Event Website Design<br>Professionally Designed Event Websites<br>Customized Look and Feel with Custom URL</p>
      <p>Registration Management Services<br>Call Center, Point of Contact<br>Housing Management, Rooming Lists<br>Data Scrubbing<br>Custom Reporting/Report Management<br>MEG will manage on your behalf, but your planners have full access</p>
      <p>Name Badges (Barcodes, Scanners)</p>
      <p>On-Site Registrars</p>
    </div>
  </div>

  <div class="sample sample--badge" role="img" aria-label="Sample attendee name badge with a city photo header"></div>
  <div class="sample sample--site" role="img" aria-label="Sample event registration web page with red header"></div>
  <div class="sample sample--page" role="img" aria-label="Sample conference website with a venue photo"></div>
  <div class="sample sample--names" role="img" aria-label="Sample printed guest and delegate badges"></div>

  <div class="slide__band-bottom"></div>
  <div class="slide__bar"></div>
</section>

</body>
</html>
```